Business card for massage therapy company called Blue Fern Wellness

Need business card for massage therapy company called Blue Fern Wellness. Would like my logo on the front and the back of the card I have 3 options of logos and you can play with what looks better.

Would like this information displayed on the back of the card:

Marcus Ellery
Licensed Massage Therapist
415-903-2264
bluefern-wellness.example
bluefern_wellness_

```html
<!DOCTYPE html>
<html lang="en">
<head>
<meta charset="utf-8">
<title>Blue Fern Wellness – Business Card</title>
<link rel="stylesheet" href="https://fonts.googleapis.com/css2?family=Josefin+Sans:wght@300;400&family=Tinos&display=swap">
<style>
  :root {
    --page-bg: #e8e5e0;
    --sage: #727862;
    --olive-ink: #6b7059;
    --tan: #c49a7c;
    --contact-ink: #6a6a66;
    --white: #ffffff;
    --watermark: #ecece7;
  }
  * { margin: 0; padding: 0; box-sizing: border-box; }
  html, body {
    width: 1189px; height: 1200px; overflow: hidden;
    background: var(--page-bg);
  }
  .card {
    position: absolute; left: 169px; width: 852px; height: 486px;
    border-radius: 26px; overflow: hidden;
    box-shadow: 0 6px 16px rgba(0,0,0,0.18);
  }
  .card--front {
    top: 112px; background: var(--sage);
    display: flex; align-items: center; justify-content: center;
  }
  .front-name {
    font-family: "Josefin Sans", sans-serif; font-weight: 300;
    color: var(--white); font-size: 54px; letter-spacing: 6px;
    text-transform: uppercase; text-align: center; line-height: 1.3;
  }
  .card--back { top: 641px; background: var(--white); }
  .watermark-ring {
    position: absolute; left: 2px; top: -37px; width: 368px; height: 368px;
    border: 3px solid var(--watermark); border-radius: 50%;
  }
  .brand {
    position: absolute; left: 455px; top: 52px; width: 400px; text-align: center;
    font-family: "Josefin Sans", sans-serif; font-weight: 400; color: var(--olive-ink);
  }
  .brand-ring {
    width: 130px; height: 130px; margin: 0 auto 22px;
    border: 2px solid var(--olive-ink); border-radius: 50%;
  }
  .brand-name { font-size: 41px; letter-spacing: 4px; line-height: 1; text-transform: uppercase; }
  .brand-sub { font-size: 23px; letter-spacing: 7px; margin-top: 12px; text-transform: uppercase; }
  .person { position: absolute; left: 58px; top: 298px; }
  .person-name {
    font-family: "Josefin Sans", sans-serif; font-weight: 300;
    font-size: 30px; letter-spacing: 1px; color: var(--olive-ink); text-transform: uppercase;
  }
  .person-title {
    font-family: "Tinos", serif; font-size: 20px; color: var(--tan);
    letter-spacing: 0.5px; margin-top: 2px;
  }
  .divider {
    position: absolute; left: 47px; top: 360px; width: 753px; height: 0;
    border-top: 1.5px solid var(--olive-ink);
  }
  .contacts { position: absolute; left: 50px; top: 375px; list-style: none; }
  .contact {
    display: flex; align-items: center; height: 27px;
    font-family: "Tinos", serif; font-size: 19px; color: var(--contact-ink); letter-spacing: 0.3px;
  }
  .contact-icon { width: 20px; height: 20px; margin-right: 9px; flex: none; }
</style>
</head>
<body>
  <section class="card card--front" aria-label="Card front">
    <h1 class="front-name">Blue Fern Wellness</h1>
  </section>

  <section class="card card--back" aria-label="Card back">
    <div class="watermark-ring" aria-hidden="true"></div>

    <div class="brand">
      <div class="brand-ring" aria-hidden="true"></div>
      <div class="brand-name">Blue Fern</div>
      <div class="brand-sub">Wellness</div>
    </div>

    <div class="person">
      <h2 class="person-name">Marcus&nbsp;&nbsp;Ellery</h2>
      <p class="person-title">Licensed Massage Therapist</p>
    </div>

    <div class="divider"></div>

    <ul class="contacts">
      <li class="contact">
        <svg class="contact-icon" viewBox="0 0 20 20" aria-hidden="true">
          <circle cx="10" cy="10" r="10" fill="#c49a7c"/>
          <path d="M7 5 L8.8 5 L9.5 7.8 L8.4 8.7 Q9.4 10.9 11.4 11.7 L12.3 10.6 L15 11.3 L15 13 Q14.5 14.8 12.5 14.5 Q7 13.3 5.6 7.5 Q5.4 5.6 7 5 Z" fill="#fff"/>
        </svg>
        415-903-2264
      </li>
      <li class="contact">
        <svg class="contact-icon" viewBox="0 0 20 20" aria-hidden="true">
          <circle cx="10" cy="10" r="10" fill="#c49a7c"/>
          <rect x="5" y="6.5" width="10" height="7" fill="none" stroke="#fff" stroke-width="1.3"/>
          <path d="M5 6.5 L10 10.5 L15 6.5" fill="none" stroke="#fff" stroke-width="1.3"/>
        </svg>
        bluefern-wellness.example
      </li>
      <li class="contact">
        <svg class="contact-icon" viewBox="0 0 20 20" aria-hidden="true">
          <circle cx="10" cy="10" r="10" fill="#c49a7c"/>
          <circle cx="10" cy="10" r="5" fill="none" stroke="#fff" stroke-width="1.1"/>
          <ellipse cx="10" cy="10" rx="2.2" ry="5" fill="none" stroke="#fff" stroke-width="1"/>
          <line x1="5" y1="10" x2="15" y2="10" stroke="#fff" stroke-width="1"/>
        </svg>
        bluefern_wellness_
      </li>
    </ul>
  </section>
</body>
</html>
```